New Business Card Design for Manufacturing

We are an engineering/manufacturing company that offers Advanced machining/assembly/engineering services, as well as innovative products for the heavy duty engine cooling markets.

We are looking to get a new business card designed that is clean and modern looking, but still fits the wide range of technical/skilled work we do.

- We hope to use this design as the base for other design work in new Presentations, web, and print work.

Industry/Entity Type

Engineering

Contact Information for Business Card

Our preferred color of blue is (RGB) 22/71/159 but can vary slightly from that color. Our content will be our Logo and full company name (Fabricated Tooling Works, Inc.), company address, name, job title, phone number with extension, cell number, fax number, website, and email address on the cards.
We'd like the full company name next to the logo, but we are open to other interpretations of that layout.
Preferably, we would like the back side to be clean with just our logo, and the front to contain all of the contact information.

Colors
2f74b4
0355a3
85abd2

Requirements
Must have
• - Logo, company name, needed content - We are open to interpretation beyond that.
• - Standard size business card.
• - Horizontal orientation.
• - Enough space for lengthy names / job titles (for example, a job title could read "Directory of Human Resources" or "V.P. of Governmental Affairs"). We need this to look clean, whether the title be short (CEO) or long (as described above).

```html
<!DOCTYPE html>
<html lang="en">
<head>
<meta charset="utf-8">
<title>Fabricated Tooling Works – Business Card</title>
<link href="https://fonts.googleapis.com/css2?family=Crimson+Pro:wght@400&family=Open+Sans:wght@400;600;800&display=swap" rel="stylesheet">
<style>
  :root{
    --brand-blue:#1647a0;
    --ink:#0a0a0b;
    --paper:#ffffff;
    --steel:#7f878c;
    --text-dark:#3a3a3a;
    --stage:#e9e7e4;
  }
  *{box-sizing:border-box;margin:0;padding:0}
  html,body{width:1200px;height:1200px;overflow:hidden;background:var(--stage)}
  .canvas{width:1200px;height:1200px;display:flex;flex-direction:column;align-items:center;justify-content:center;gap:56px}
  .card{position:relative;width:900px;height:514px;overflow:hidden;box-shadow:0 6px 18px rgba(0,0,0,.18)}

  /* shared accent strip */
  .accent-band{position:absolute;left:0;right:0;bottom:0;height:40px;background:var(--brand-blue)}
  .accent-steel{position:absolute;right:120px;bottom:40px;width:92px;height:34px;background:var(--steel)}
  .accent-tab{position:absolute;right:0;bottom:40px;width:112px;height:34px;background:var(--brand-blue)}

  /* back */
  .card-back{background:var(--ink)}
  .back-mark{position:absolute;left:150px;top:168px;display:flex;align-items:center;gap:22px;color:var(--paper);font-family:"Open Sans",sans-serif;font-weight:800}
  .back-mark .mark-square{width:74px;height:74px;background:var(--paper)}
  .back-mark .mark-name{font-size:34px;line-height:1.08;letter-spacing:.5px;text-transform:uppercase}

  /* front */
  .card-front{background:var(--paper);font-family:"Open Sans",sans-serif;color:var(--text-dark)}
  .front-mark{position:absolute;left:0;right:0;top:48px;text-align:center;color:var(--brand-blue);font-weight:800;font-size:34px;letter-spacing:.5px;text-transform:uppercase}
  .rule{position:absolute;height:1px;background:var(--brand-blue)}
  .rule-top{left:150px;right:0;top:150px}
  .rule-mid{left:150px;right:0;top:212px}
  .rule-low{left:150px;right:80px;top:262px}
  .identity{position:absolute;left:150px;top:162px;display:flex;align-items:baseline;gap:12px;font-size:17px;white-space:nowrap}
  .person-name{font-family:"Crimson Pro",serif;font-size:40px;color:var(--brand-blue);line-height:1}
  .sep{color:#555}
  .company-name{position:absolute;left:150px;top:222px;font-size:20px;font-weight:600;letter-spacing:1px;color:var(--brand-blue)}
  .contact-row{position:absolute;left:0;right:0;display:flex;justify-content:center;align-items:center;gap:10px;font-size:18px;white-space:nowrap}
  .row-address{top:300px}
  .row-phone{top:350px}
  .ext{color:var(--brand-blue)}
  .icon{width:20px;height:20px;flex:none}
</style>
</head>
<body>
<main class="canvas">

  <section class="card card-back" aria-label="Card back">
    <div class="back-mark">
      <span class="mark-square"></span>
      <span class="mark-name">Fabricated<br>Tooling Works<br>Inc.</span>
    </div>
    <div class="accent-steel"></div>
    <div class="accent-tab"></div>
    <div class="accent-band"></div>
  </section>

  <section class="card card-front" aria-label="Card front">
    <div class="front-mark">Fabricated Tooling Works</div>

    <div class="rule rule-top"></div>
    <div class="identity">
      <span class="person-name">Daniel Reyes</span>
      <span class="sep">|</span><span>Director</span>
      <span class="sep">|</span>
      <svg class="icon" viewBox="0 0 20 20"><rect width="20" height="20" rx="3" fill="#1647a0"/><rect x="7" y="4" width="6" height="12" rx="1" fill="none" stroke="#fff" stroke-width="1.6"/></svg>
      <span>1-555 014 2280</span>
      <span class="sep">|</span>
      <svg class="icon" viewBox="0 0 20 20"><rect width="20" height="20" rx="3" fill="#1647a0"/><circle cx="10" cy="10" r="5.5" fill="none" stroke="#fff" stroke-width="1.4"/><path d="M4.5 10h11M10 4.5v11" stroke="#fff" stroke-width="1.2"/></svg>
      <span>www.ftworks.com</span>
    </div>
    <div class="rule rule-mid"></div>
    <div class="company-name">Fabricated Tooling Works, Inc.</div>
    <div class="rule rule-low"></div>

    <div class="contact-row row-address">
      <svg class="icon" viewBox="0 0 20 20"><rect width="20" height="20" rx="3" fill="#1647a0"/><path d="M10 16s-4.5-4.6-4.5-7.5a4.5 4.5 0 0 1 9 0C14.5 11.4 10 16 10 16z" fill="#fff"/><circle cx="10" cy="8.5" r="1.6" fill="#1647a0"/></svg>
      <span>Harbor Falls, Westmark</span>
      <span class="sep">|</span>
      <svg class="icon" viewBox="0 0 20 20"><rect width="20" height="20" rx="3" fill="#1647a0"/><rect x="5" y="8" width="10" height="7" rx="1" fill="#fff"/><rect x="7" y="4" width="6" height="4" fill="none" stroke="#fff" stroke-width="1.4"/></svg>
      <span>1-555 014 2290</span>
      <span class="sep">|</span>
      <svg class="icon" viewBox="0 0 20 20"><rect width="20" height="20" rx="3" fill="#1647a0"/><rect x="4" y="6" width="12" height="8" fill="#fff"/><path d="M4 6l6 5 6-5" fill="none" stroke="#1647a0" stroke-width="1.3"/></svg>
      <span>daniel@ftworks.com</span>
    </div>

    <div class="contact-row row-phone">
      <svg class="icon" viewBox="0 0 20 20"><rect width="20" height="20" rx="3" fill="#1647a0"/><path d="M6 5c1 0 2 2 2 3s-1 1-1 1.5 2 3.5 3.5 3.5c.5 0 .5-1 1.5-1s3 1 3 2-1.5 2-2.5 2C8 16 4 12 4 7c0-1 1-2 2-2z" fill="#fff"/></svg>
      <span>1-555-014-2200 <span class="ext">(EXT)</span></span>
    </div>

    <div class="accent-steel"></div>
    <div class="accent-tab"></div>
    <div class="accent-band"></div>
  </section>

</main>
</body>
</html>
```